'Vessel types, Demand, Supply & Disruptions - what's currently driving the bulk shipping

This is required for a talk that needs to cover the following matters

the difference between small, handysize, handymax, panamax, capesize, and very large bulk carriers, how the trade differs, self loading/unloading etc as an intro to the dry bulk trade and what's currently driving the bulk shipping markets.

The below is an initial breakdown on the slides but not finalised

There will need to be an additional slide on the importance of China for the dry bulk trades

Slide 1: Introduction

Welcome and brief overview of dry bulk shipping
Importance in global trade and economy
Slide 2: Types of Dry Bulk Vessels

Capesize: 100,000-400,000 DWT
Panamax: 60,000-100,000 DWT
Supramax: 45,000-60,000 DWT
Handysize: 15,000-45,000 DWT
Description and key features of each vessel type
Slide 3: Vessel Characteristics

Holds and hatches
Draft, beam, and length
Cargo handling equipment
Engine types and power
Slide 4: Routing in Dry Bulk Shipping

Major shipping routes (e.g., Cape of Good Hope, Panama Canal)
Factors influencing routing decisions (e.g., weather, fuel costs)
Strategic chokepoints and canals
Slide 5: Fixing and Chartering

Voyage Charter
Owner's responsibility
Charterer's responsibility
Time Charter
Bareboat Charter
Spot and long-term contracts
Slide 6: Key Charter Party (CP) Terms

Laytime and demurrage
Freight rates
Notice of Readiness (NOR)
Cargo quantities and quality
Ballast bonus
Slide 7: Current Disruptions in Dry Bulk Shipping

Impact of geopolitical events (e.g., trade tensions, conflicts) on shipping lanes
Effects of economic downturns (e.g., COVID-19 pandemic) on demand and supply chains
Environmental regulations affecting vessel operations
Port congestion and delays
Slide 8: Market Trends and Innovations

Technological advancements in vessel design (e.g., eco-friendly propulsion systems, fuel efficiency)
Digitalization and smart shipping solutions
Sustainability initiatives in the industry (e.g., ballast water treatment, emissions reduction)
Slide 9: Mitigation Strategies for Disruptions

Diversification of trading routes and markets
Investment in fleet optimization and efficiency measures
Collaboration with industry partners and stakeholders to address common challenges
Continuous monitoring and adaptation to changing market conditions
Slide 10: Case Study

Example of a recent disruption and its impact on dry bulk shipping operations
Lessons learned and strategies employed to mitigate the effects
Slide 11: Future Outlook

Anticipated trends and challenges in the dry bulk shipping industry
Opportunities for innovation and growth
Importance of sustainability and resilience in shaping the future of the industry
Slide 12: Conclusion

Recap of key points
Call to action for stakeholders to collaborate and innovate for a sustainable and resilient dry bulk shipping industry
Slide 13: Q&A

```html
<!DOCTYPE html>
<html lang="en">
<head>
<meta charset="utf-8">
<title>Vessel Type, Demand, Supply &amp; Disruption</title>
<link rel="stylesheet" href="https://fonts.googleapis.com/css2?family=Rubik:wght@400;500;600&family=Inter:wght@400;500;600;700&display=swap">
<style>
:root{
  --navy:#0b3161;
  --navy-deep:#06284f;
  --ink:#13294a;
  --text:#5b6577;
  --cyan:#35b4dc;
  --sea:#1f6fb0;
  --rule:#9cc9d6;
  --card:#f5f9fe;
  --page-top:#f7faff;
  --page-bottom:#dceafa;
  --white:#ffffff;
}
*{margin:0;padding:0;box-sizing:border-box}
html,body{width:1200px;height:3152px;overflow:hidden}
body{
  background:linear-gradient(180deg,#f6f9fe 0%,#e6eefa 60%,#dbe7f8 100%);
  font-family:"Inter",sans-serif;color:var(--ink);position:relative;
}
.slide{
  position:absolute;left:106px;width:988px;height:556px;overflow:hidden;
  background:linear-gradient(180deg,var(--page-top) 0%,var(--page-bottom) 100%);
  box-shadow:0 24px 40px rgba(40,70,120,.16);
}
.abs{position:absolute}
.brand{font-family:"Rubik",sans-serif;font-weight:600;font-size:22px;letter-spacing:.02em;display:flex;align-items:center;gap:8px}
.brand-dot{width:12px;height:12px;border-radius:50%;background:currentColor}

/* cover */
.cover{top:105px;background:linear-gradient(160deg,#24508a 0%,#1c4a82 40%,#2a5f93 70%,#345f88 100%)}
.cover .photo{inset:0}
.cover .brand{color:var(--white);left:0;right:0;top:124px;justify-content:center}
.cover-title{left:0;right:0;top:200px;text-align:center;color:var(--white);font-family:"Rubik",sans-serif;font-weight:500;font-size:36px;line-height:49px;letter-spacing:.01em}
.cover-name{left:0;right:0;top:360px;text-align:center;color:var(--white);font-family:"Inter",sans-serif;font-weight:600;font-size:19px}
.cover-foot{top:502px;color:#e3edf8;font-size:15px}

/* title slide */
.title-slide{top:701px;background:linear-gradient(180deg,#ffffff 0%,#dbe9fa 100%)}
.hero-circle{left:64px;top:109px;width:358px;height:358px;border-radius:50%;border:5px solid #fff;
  background:radial-gradient(circle at 55% 50%,#2b7fc0 0%,#1a5e9e 60%,#12457c 100%);box-shadow:0 8px 20px rgba(0,0,0,.15)}
.title-main{left:551px;top:168px;font-family:"Rubik",sans-serif;font-weight:500;font-size:33px;line-height:44px;color:var(--navy)}
.title-meta{left:551px;top:332px;font-family:"Inter",sans-serif;font-weight:600;font-size:20px;color:var(--cyan);word-spacing:3px}
.title-meta span+span{margin-left:14px}
.title-web{right:48px;top:498px;color:#fff;font-size:16px}

/* content slides */
.intro{top:1297px}.types{top:1894px}.traits{top:2490px}
.slide-heading{left:64px;top:38px;font-family:"Rubik",sans-serif;font-weight:500;font-size:27px;color:var(--navy)}
.slide-brand{right:70px;top:40px;color:var(--sea);font-size:19px}
.slide-rule{left:64px;right:64px;top:94px;height:1px;background:var(--rule)}
.footer-name{left:72px;top:518px;font-size:11px;font-weight:700;color:var(--ink)}
.footer-page{right:66px;top:512px;display:flex;align-items:center;gap:12px;font-size:11px;font-weight:700;color:var(--ink)}
.footer-page i{display:block;width:2px;height:22px;background:var(--navy)}

.intro-lead{left:64px;top:178px;width:400px;font-family:"Inter",sans-serif;font-weight:600;font-size:20px;line-height:37px;color:var(--ink)}
.stat{top:315px;width:125px;height:91px;background:var(--card);box-shadow:0 8px 16px rgba(40,70,120,.15);text-align:center;padding-top:22px}
.stat b{display:block;font-family:"Rubik",sans-serif;font-weight:500;font-size:21px;color:var(--navy)}
.stat small{display:block;margin-top:4px;font-size:11px;color:var(--text)}
.intro-photo{left:522px;top:148px;width:466px;height:281px;background:linear-gradient(180deg,#c9d3dc 0%,#b7c2cd 35%,#2f86c0 62%,#a9b4be 78%,#c5ccd3 100%)}

.type-card{top:174px;width:208px;height:287px;background:var(--card);box-shadow:0 8px 18px rgba(40,70,120,.16);text-align:center}
.type-ship{top:-38px;left:37px;width:134px;height:62px;border-radius:4px 4px 18px 18px;background:linear-gradient(180deg,#7a4d4a 0%,#3f5f82 55%,#39a9cf 78%,#1f4f80 100%)}
.type-name{margin-top:52px;font-family:"Rubik",sans-serif;font-weight:500;font-size:24px;color:#4a5260}
.type-dwt{margin-top:8px;font-size:12px;font-weight:600;color:var(--cyan)}
.type-body{margin:18px 16px 0;font-size:11.5px;line-height:19px;color:var(--text);text-align:justify}

.traits-block{left:0;top:237px;width:400px;height:173px;background:var(--navy)}
.traits-photo{left:0;top:163px;width:500px;height:230px;border-radius:0 0 60px 0;background:linear-gradient(180deg,#c7443f 0%,#3b4f74 30%,#6b6f86 55%,#48a9cf 80%,#b0243f 100%);box-shadow:0 10px 20px rgba(0,0,0,.2)}
.trait{left:604px;width:340px}
.trait h3{font-family:"Inter",sans-serif;font-weight:600;font-size:14.5px;color:#3b4656;display:flex;align-items:center;gap:14px;margin-left:-6px}
.trait h3::before{content:"";width:24px;height:5px;border-radius:3px;background:var(--sea)}
.trait ul{list-style:none;margin-left:40px}
.trait li{font-size:12px;color:var(--text);line-height:25px}
.trait li::before{content:"•";margin-right:9px}
</style>
</head>
<body>

<section class="slide cover">
  <div class="abs photo" role="img" aria-label="Container ship sailing at sea, tinted deep blue"></div>
  <div class="abs brand"><span class="brand-dot"></span>Keelway</div>
  <h1 class="abs cover-title">VESSEL TYPE, DEMAND,<br>SUPPLY &amp; DISRUPTION</h1>
  <p class="abs cover-name">Mara Lindqvist</p>
  <p class="abs cover-foot" style="left:56px">March 2024</p>
  <p class="abs cover-foot" style="right:56px">website.com</p>
</section>

<section class="slide title-slide">
  <svg class="abs" style="left:0;top:0" width="988" height="556" viewBox="0 0 988 556">
    <path d="M0 370 C 180 400, 320 445, 520 455 C 760 468, 920 440, 988 368 L988 556 L0 556 Z" fill="var(--navy)"/>
  </svg>
  <div class="abs hero-circle" role="img" aria-label="Aerial view of a tanker and tug on deep blue water"></div>
  <h1 class="abs title-main">VESSEL TYPE, DEMAND,<br>SUPPLY &amp; DISRUPTION</h1>
  <p class="abs title-meta"><span>Mara Lindqvist</span><span>March 2024</span></p>
  <p class="abs title-web">website.com</p>
</section>

<section class="slide intro">
  <h2 class="abs slide-heading">Introduction</h2>
  <div class="abs brand slide-brand"><span class="brand-dot"></span>Keelway</div>
  <div class="abs slide-rule"></div>
  <p class="abs intro-lead">Welcome and Brief Overview Of Dry Bulk Shipping Importance In Global Trade and Economy</p>
  <div class="abs stat" style="left:61px"><b>34</b><small>Years Operation</small></div>
  <div class="abs stat" style="left:203px"><b>28+</b><small>Courier Brand</small></div>
  <div class="abs stat" style="left:345px"><b>+400M</b><small>Cargo</small></div>
  <div class="abs intro-photo" role="img" aria-label="Loaded container ship passing a wooded shoreline"></div>
  <p class="abs footer-name">Mara Lindqvist</p>
  <div class="abs footer-page">Page<i></i>3</div>
</section>

<section class="slide types">
  <h2 class="abs slide-heading">Vessel Type</h2>
  <div class="abs brand slide-brand"><span class="brand-dot"></span>Keelway</div>
  <div class="abs slide-rule"></div>

  <article class="abs type-card" style="left:61px">
    <div class="abs type-ship" role="img" aria-label="Container ship"></div>
    <h3 class="type-name">Capesize</h3>
    <p class="type-dwt">100,000-400,000 DWT</p>
    <p class="type-body">Lorem ipsum dolor sit amet, in consectetuer adipiscing elit. Maecenas porttitor congue o massa. Fusce posuere, magna sed pulvinar ultricies, purus lectus malesuada libero, sit amet commodo magna ero.</p>
  </article>
  <article class="abs type-card" style="left:280px">
    <div class="abs type-ship" role="img" aria-label="Container ship"></div>
    <h3 class="type-name">Panamax</h3>
    <p class="type-dwt">60,000-100,000 DWT</p>
    <p class="type-body">Lorem ipsum dolor sit amet, in consectetuer adipiscing elit. Maecenas porttitor congue o massa. Fusce posuere, magna sed pulvinar ultricies, purus lectus malesuada libero, sit amet commodo magna ero.</p>
  </article>
  <article class="abs type-card" style="left:499px">
    <div class="abs type-ship" role="img" aria-label="Container ship"></div>
    <h3 class="type-name">Supramax</h3>
    <p class="type-dwt">45,000-60,000 DWT</p>
    <p class="type-body">Lorem ipsum dolor sit amet, in consectetuer adipiscing elit. Maecenas porttitor congue o massa. Fusce posuere, magna sed pulvinar ultricies, purus lectus malesuada libero, sit amet commodo magna ero.</p>
  </article>
  <article class="abs type-card" style="left:719px">
    <div class="abs type-ship" role="img" aria-label="Container ship"></div>
    <h3 class="type-name">Handysize</h3>
    <p class="type-dwt">15,000-45,000 DWT</p>
    <p class="type-body">Lorem ipsum dolor sit amet, in consectetuer adipiscing elit. Maecenas porttitor congue o massa. Fusce posuere, magna sed pulvinar ultricies, purus lectus malesuada libero, sit amet commodo magna ero.</p>
  </article>

  <p class="abs footer-name">Mara Lindqvist</p>
  <div class="abs footer-page">Page<i></i>4</div>
</section>

<section class="slide traits">
  <h2 class="abs slide-heading">Vessel Characteristics</h2>
  <div class="abs brand slide-brand"><span class="brand-dot"></span>Keelway</div>
  <div class="abs slide-rule"></div>
  <div class="abs traits-block"></div>
  <div class="abs traits-photo" role="img" aria-label="Fully loaded container ship seen from the side"></div>

  <div class="abs trait" style="top:127px">
    <h3>Holds and Hatches</h3>
    <ul><li>Lorem ipsum dolor sit amet,</li><li>Lorem ipsum dolor sit amet,</li></ul>
  </div>
  <div class="abs trait" style="top:225px">
    <h3>Draft, Beam, and Length</h3>
    <ul><li>Up to 98,000 DWT</li><li>300 m (980 ft)</li><li>40 m (130 ft)</li></ul>
  </div>
  <div class="abs trait" style="top:341px">
    <h3>Cargo Handling Equipment</h3>
    <ul><li>Lorem ipsum dolor sit amet,</li><li>Lorem ipsum dolor sit amet,</li></ul>
  </div>
  <div class="abs trait" style="top:436px">
    <h3>Engine</h3>
    <ul><li>2-stroke diesel engine and 1 propeller</li></ul>
  </div>

  <p class="abs footer-name">Mara Lindqvist</p>
  <div class="abs footer-page">Page<i></i>5</div>
</section>

</body>
</html>
```